Brannock Bay Ferry and Haulage

Need to redesign our business cards to relay that we do freight logistics and water taxi service. We also work with gov. agencies doing environmental clean up, oil spill response, remote site construction and work with many of the air taxi and helicopter services on Kodiak Island. Out website is www.brannockbayferry.com to get a better idea of what we do.

Contact Information for Business Card

I have a previous business card but it just has the logo on the front, and a sunset picture on the back with the contact info. It does not relay what we do and what we can help with. I like a simple straight forward design over a busy one.

Colors
3176b5
0455a3
cfdfed

Requirements
Must have
• logo, email, website, phone number

```html
<!DOCTYPE html>
<html lang="en">
<head>
<meta charset="utf-8">
<title>Brannock Bay Ferry and Haulage — Business Cards</title>
<link href="https://fonts.googleapis.com/css2?family=Montserrat:wght@500;600;700&family=Open+Sans:wght@400;600&display=swap" rel="stylesheet">
<style>
  :root{
    --bg:#e6ecf3;
    --brand-blue:#0455a3;
    --brand-blue-mid:#3176b5;
    --brand-blue-pale:#cfdfed;
    --accent-orange:#f5a21b;
    --ink:#2d2d2d;
    --rule:#1a1a1a;
    --paper:#ffffff;
  }
  *{box-sizing:border-box;margin:0;padding:0}
  html,body{width:1200px;height:892px;overflow:hidden;background:var(--bg)}
  .canvas{position:relative;width:1200px;height:892px}

  .card{position:absolute;width:560px;height:320px;box-shadow:0 10px 28px rgba(20,40,70,.22);overflow:hidden}

  /* back side */
  .card--back{left:50px;top:90px;background:linear-gradient(135deg,var(--brand-blue-mid) 0%,var(--brand-blue) 60%,#034a8f 100%)}
  .back-mark{position:absolute;left:0;right:0;top:92px;display:flex;align-items:center;justify-content:center;gap:14px}
  .back-mark__dot{width:26px;height:26px;border-radius:50%;background:var(--accent-orange)}
  .back-mark__name{font-family:"Montserrat",sans-serif;font-weight:700;font-size:27px;color:#fff;letter-spacing:.5px;line-height:1.15}
  .back-services{position:absolute;left:0;right:0;top:182px;text-align:center;font-family:"Montserrat",sans-serif;font-weight:500;font-size:13px;letter-spacing:1.5px;color:var(--brand-blue-pale);text-transform:uppercase}
  .back-url{position:absolute;left:0;right:0;bottom:46px;text-align:center;font-family:"Open Sans",sans-serif;font-size:14px;letter-spacing:5px;color:#fff}

  /* front side */
  .card--front{left:590px;top:470px;background:var(--paper)}
  .front-mark{position:absolute;right:34px;top:26px;text-align:right}
  .front-mark__row{display:flex;align-items:center;justify-content:flex-end;gap:10px}
  .front-mark__dot{width:18px;height:18px;border-radius:50%;background:var(--accent-orange)}
  .front-mark__name{font-family:"Montserrat",sans-serif;font-weight:700;font-size:19px;color:var(--brand-blue);line-height:1.15}
  .front-mark__services{font-family:"Open Sans",sans-serif;font-size:11.5px;color:var(--ink);margin-top:5px;letter-spacing:.2px}
  .front-rule{position:absolute;left:250px;right:28px;top:116px;height:1.5px;background:var(--rule)}

  .holder{position:absolute;left:34px;top:166px}
  .holder__name{font-family:"Montserrat",sans-serif;font-weight:700;font-size:21px;color:var(--brand-blue);letter-spacing:.3px;line-height:1.2}
  .holder__title{font-family:"Montserrat",sans-serif;font-weight:500;font-size:14px;color:var(--accent-orange);margin-top:1px}
  .holder__rule{width:260px;height:1px;background:var(--rule);margin:8px 0 8px}

  .contact-list{list-style:none;font-family:"Open Sans",sans-serif;font-size:13.5px;color:var(--ink)}
  .contact-list li{display:flex;align-items:center;gap:10px;height:19px}
  .contact-list svg{width:14px;height:14px;fill:var(--brand-blue);flex:none}

  .band{position:absolute;left:0;right:0;bottom:0}
  .band__stripe{height:4px;background:var(--accent-orange)}
  .band__gap{height:3px;background:var(--paper)}
  .band__fill{height:16px;background:var(--brand-blue)}
</style>
</head>
<body>
<main class="canvas">

  <section class="card card--back" aria-label="Business card, back">
    <div class="back-mark">
      <span class="back-mark__dot"></span>
      <span class="back-mark__name">Brannock Bay<br>Ferry and Haulage</span>
    </div>
    <p class="back-services">Freight · Water Taxi · Spill Response · Remote Sites</p>
    <p class="back-url">www.brannockbayferry.com</p>
  </section>

  <section class="card card--front" aria-label="Business card, front">
    <div class="front-mark">
      <div class="front-mark__row">
        <span class="front-mark__dot"></span>
        <span class="front-mark__name">Brannock Bay<br>Ferry and Haulage</span>
      </div>
      <p class="front-mark__services">Freight · Water Taxi · Spill Response</p>
    </div>
    <div class="front-rule"></div>

    <div class="holder">
      <h1 class="holder__name">MARA ELLISON</h1>
      <p class="holder__title">PRESIDENT</p>
      <div class="holder__rule"></div>
      <ul class="contact-list">
        <li>
          <svg viewBox="0 0 24 24" aria-hidden="true"><path d="M6.6 10.8a15.1 15.1 0 0 0 6.6 6.6l2.2-2.2a1 1 0 0 1 1-.25 11.4 11.4 0 0 0 3.6.57 1 1 0 0 1 1 1V20a1 1 0 0 1-1 1A17 17 0 0 1 3 4a1 1 0 0 1 1-1h3.5a1 1 0 0 1 1 1c0 1.25.2 2.45.57 3.57a1 1 0 0 1-.25 1z"/></svg>
          555 0142 7788
        </li>
        <li>
          <svg viewBox="0 0 24 24" aria-hidden="true"><path d="M2 5h20v14H2z M3.5 6.5 12 13l8.5-6.5" fill="none" stroke="#0455a3" stroke-width="2"/><path d="M2 5h20v3l-10 7L2 8z"/></svg>
          mara@brannockbayferry.com
        </li>
        <li>
          <svg viewBox="0 0 24 24" aria-hidden="true"><circle cx="12" cy="12" r="10"/><path d="M2 12h20M12 2c3 3 3 17 0 20M12 2c-3 3-3 17 0 20" fill="none" stroke="#fff" stroke-width="1.5"/></svg>
          www.brannockbayferry.com
        </li>
      </ul>
    </div>

    <div class="band">
      <div class="band__stripe"></div>
      <div class="band__gap"></div>
      <div class="band__fill"></div>
    </div>
  </section>

</main>
</body>
</html>
```